Vellora Labs - Mushroom Supplement Packaging

Our brand is called Vellora Labs. I've added a couple different logos that you can use. We are creating a line up of Mushroom Supplement products. I will add the entire line-up of products here. I've added examples of other products and packaging shape types I can purchase. Give me different options for packaging that is minimalist and clean for this brand that makes it look really well made and clean and make people want to buy.

Product 1 Lions Mane 1g
Product 2 Cordyceps 1g
Product 3 Chaga 1g
Product 4 Turkey Tail 1g
Product 5 Reishi 1g
Product 6 Maitake 1g
Product 7 Shiitake 1g

Product 8 (Mix) Lions Mane 143mg
Cordyceps 143mg
Chaga 143mg
Turkey Tail 143mg
Reishi 143mg
Maitake 143mg
Shiitake 143mg

```html
<!DOCTYPE html>
<html lang="en">
<head>
<meta charset="utf-8">
<title>Vellora Labs – Lions Mane Label</title>
<link rel="stylesheet" href="https://fonts.googleapis.com/css2?family=Comfortaa:wght@500&family=Barlow+Semi+Condensed:wght@600;700;800&display=swap">
<style>
  :root {
    --backdrop: #b5865a;
    --label: #ffffff;
    --ink: #2a1e17;
    --bar-start: #4a382c;
    --bar-end: #1f140e;
    --accent: #b8875a;
    --placeholder-top: #d9824e;
    --placeholder-bottom: #e9dccd;
  }
  * { box-sizing: border-box; margin: 0; padding: 0; }
  html, body {
    width: 1200px;
    height: 900px;
    overflow: hidden;
    background: var(--backdrop);
  }
  .label {
    position: absolute;
    left: 240px;
    top: 50px;
    width: 720px;
    height: 800px;
    background: var(--label);
  }
  .brand {
    position: absolute;
    top: 150px;
    left: 0;
    width: 100%;
    text-align: center;
    font-family: "Barlow Semi Condensed", sans-serif;
    font-weight: 800;
    font-size: 58px;
    letter-spacing: 1px;
    color: var(--ink);
    text-transform: uppercase;
  }
  .product-name {
    position: absolute;
    top: 268px;
    left: 100px;
    width: 500px;
    font-family: "Comfortaa", sans-serif;
    font-weight: 500;
    font-size: 84px;
    letter-spacing: 0;
    color: var(--ink);
    line-height: 1;
    white-space: nowrap;
  }
  .dose-badge {
    position: absolute;
    top: 200px;
    left: 612px;
    width: 86px;
    height: 86px;
    border-radius: 50%;
    background: var(--accent);
    color: var(--label);
    font-family: "Barlow Semi Condensed", sans-serif;
    font-weight: 800;
    font-size: 38px;
    display: flex;
    align-items: center;
    justify-content: center;
  }
  .strain-bar {
    position: absolute;
    top: 372px;
    left: 95px;
    width: 500px;
    height: 46px;
    background: linear-gradient(90deg, var(--bar-start), var(--bar-end));
    color: var(--label);
    font-family: "Barlow Semi Condensed", sans-serif;
    font-weight: 700;
    font-size: 22px;
    letter-spacing: 0.5px;
    display: flex;
    align-items: flex-end;
    justify-content: center;
    padding-bottom: 3px;
  }
  .product-visual {
    position: absolute;
    top: 455px;
    left: 225px;
    width: 270px;
    height: 245px;
    border-radius: 120px 120px 16px 16px;
    background: linear-gradient(180deg, var(--placeholder-top), var(--placeholder-bottom));
  }
  .contents-line {
    position: absolute;
    bottom: 42px;
    left: 0;
    width: 100%;
    text-align: center;
    font-family: "Barlow Semi Condensed", sans-serif;
    font-weight: 700;
    font-size: 24px;
    letter-spacing: 0.5px;
    color: var(--ink);
    text-transform: uppercase;
  }
</style>
</head>
<body>
  <main class="label">
    <div class="brand">Vellora Labs</div>
    <div class="dose-badge">1G</div>
    <h1 class="product-name">lions mane</h1>
    <div class="strain-bar">CORDYCEPS 143MG</div>
    <div class="product-visual" role="img" aria-label="Illustration of a mushroom with supplement capsules at its base"></div>
    <p class="contents-line">Dietary Supplements 120 Capsules</p>
  </main>
</body>
</html>
```